Webdesign für eine Softwarewarentwicklung und Consulting für das Gesundheitswesen
Zielgruppe
Softwarewarentwicklung und Consulting für das Gesundheitswesen. Unsere Zielgruppe sind Unternehmen und Organisationen im Bereich des Gesundheitswesen. Weiter informationen auf derzeitiger Homepage unter www.vmt-pflegeloesung.de.
Aufgabenstellung
Das Webdesign sollte deutlich moderner und kreativer wirken als unsere derzeitige Hompage. (Die bisherige Hompage wurde seinerzeit bei der Gründung 'auf die Schnelle' entwickelt.) Die neue Homapage sollte 'frisch' wirken und einem modernen Softwareunternehmen entsprechen.: Schlicht, modern und innovativ. Die Website sollte auch später gut auf Handy und Tablet darstellbar sein. Da wir derzeit wenig Inhalte auf unserer Homepage haben, wären wir auch für inhaltliche Vorschläge dankbar. Unsere Logofarben sollten sich auch im Design wiederfinden (der Rotton hat den Wert RGB: 227, 7, 19 #e30713 - der Blauton hat den Wert RGB: 30, 38, 74 1 #e264a).
Im Format bin ich unerfahren und würde dann für das spätere Umsetzen Adobe Photoshop vorschlagen.
Idealerweise sollte sich das Design später in einem gängigen CMS umsetzen lassen.
Gerne können Sie uns auch ein Komplettangebot auch zum Thema Umsetzung unterbreiten.
Grundsätzlich finde ich folgende Hompages ganz gut:
https://brelvuno.com/
https://www.kiesfeld.de/
https://www.plumvantic.com/de/
https://zirkanu.de/

```html
<!DOCTYPE html>
<html lang="de">
<head>
<meta charset="utf-8">
<title>VMT – Softwareentwicklung für das Gesundheitswesen</title>
<link rel="stylesheet" href="https://fonts.googleapis.com/css2?family=Open+Sans:wght@400;600;700;800&display=swap">
<style>
  :root {
    --red: #e30713;
    --navy: #1b2139;
    --grey-band: #9b9b9b;
    --white: #ffffff;
    --ink: #111111;
    --heading-light: #dadada;
  }
  * { box-sizing: border-box; margin: 0; padding: 0; }
  html, body { width: 1170px; height: 1200px; overflow: hidden; }
  body { position: relative; font-family: "Open Sans", Arial, sans-serif; color: var(--ink); background: var(--white); }

  .site-header { position: absolute; left: 0; top: 0; width: 1170px; height: 156px; background: var(--white); }
  .header-phone { position: absolute; left: 56px; top: 34px; font-size: 19px; display: flex; align-items: center; gap: 6px; }
  .brand { position: absolute; left: 50%; top: 20px; transform: translateX(-50%); display: flex; align-items: center; gap: 8px; }
  .brand-mark { width: 14px; height: 14px; background: var(--red); }
  .brand-name { font-size: 40px; font-weight: 800; color: var(--navy); letter-spacing: 1px; line-height: 1; }
  .menu-toggle { position: absolute; left: 1068px; top: 30px; width: 32px; }
  .menu-toggle span { display: block; height: 3px; background: var(--ink); margin-bottom: 7px; }
  .tagline { position: absolute; left: 0; top: 92px; width: 100%; text-align: center; font-size: 28px; color: var(--navy); }

  .contact-band { position: absolute; left: 0; top: 156px; width: 1170px; height: 688px; background: var(--grey-band); }

  .message-panel { position: absolute; left: 456px; top: 79px; width: 662px; height: 581px; background: var(--navy); box-shadow: 0 6px 18px rgba(0,0,0,.35); }
  .message-panel h2 { position: absolute; left: 130px; top: 82px; width: 440px; text-align: center; font-size: 56px; font-weight: 700; color: var(--heading-light); line-height: 1.2; }
  .field { position: absolute; left: 118px; width: 462px; background: var(--white); font-size: 14px; color: #777; padding: 0 12px; display: flex; align-items: center; }
  .submit { position: absolute; left: 289px; top: 449px; width: 119px; height: 43px; background: var(--red); color: var(--white); font-size: 15px; font-weight: 700; letter-spacing: 1px; display: flex; align-items: center; justify-content: center; }

  .info-card { position: absolute; background: var(--white); text-align: center; }
  .info-card svg { display: block; margin: 0 auto; }
  .info-card h3 { font-size: 22px; font-weight: 700; margin-top: 14px; letter-spacing: .3px; }
  .info-card p { font-size: 15px; line-height: 24px; margin-top: 14px; }
  .info-card a { color: var(--red); }

  .site-footer { position: absolute; left: 0; top: 844px; width: 1170px; height: 356px; background: var(--navy); color: var(--white); }
  .footer-brand { position: absolute; left: 50%; top: 42px; transform: translateX(-50%); background: var(--white); padding: 4px 14px; font-size: 28px; font-weight: 800; color: var(--navy); line-height: 1.2; }
  .footer-social { position: absolute; left: 560px; top: 110px; display: flex; gap: 10px; }
  .footer-social span { width: 20px; height: 20px; background: var(--red); border-radius: 50%; }
  .footer-social span.square { border-radius: 4px; background: #f08a2c; }
  .footer-rule { position: absolute; left: 56px; top: 158px; width: 1062px; height: 2px; background: var(--white); }
  .footer-col { position: absolute; top: 186px; font-size: 15px; font-weight: 700; line-height: 24px; }
</style>
</head>
<body>
  <header class="site-header">
    <div class="header-phone">
      <svg width="18" height="18" viewBox="0 0 24 24"><path fill="#888" d="M6.6 10.8a15 15 0 0 0 6.6 6.6l2.2-2.2c.3-.3.7-.4 1-.2 1.1.4 2.3.6 3.6.6.6 0 1 .4 1 1V20c0 .6-.4 1-1 1A17 17 0 0 1 3 4c0-.6.4-1 1-1h3.5c.6 0 1 .4 1 1 0 1.3.2 2.5.6 3.6.1.3 0 .7-.2 1z"/></svg>
      +1 (555) 014-2290
    </div>
    <div class="brand"><span class="brand-mark"></span><span class="brand-name">VMT</span></div>
    <div class="menu-toggle"><span></span><span></span><span></span></div>
    <p class="tagline">Softwareentwicklung für das Gesundheitswesen</p>
  </header>

  <section class="contact-band">
    <div class="message-panel">
      <h2>Ihre Nachricht</h2>
      <div class="field" style="top:171px;height:41px">Enter your Name</div>
      <div class="field" style="top:238px;height:41px">Enter a valid email address</div>
      <div class="field" style="top:307px;height:114px"></div>
      <div class="submit">SUBMIT</div>
    </div>

    <div class="info-card" style="left:56px;top:131px;width:227px;height:238px;padding-top:28px">
      <svg width="44" height="58" viewBox="0 0 24 32"><path fill="var(--red)" d="M12 0C5.4 0 0 5.2 0 11.7 0 20.5 12 32 12 32s12-11.5 12-20.3C24 5.2 18.6 0 12 0zm0 16a4.5 4.5 0 1 1 0-9 4.5 4.5 0 0 1 0 9z"/></svg>
      <h3>ANSCHRIFT</h3>
      <p>Lindenweg 17<br>40210 Ortsbach</p>
    </div>
    <div class="info-card" style="left:304px;top:131px;width:229px;height:238px;padding-top:28px">
      <svg width="58" height="58" viewBox="0 0 24 24"><path fill="var(--red)" d="M6.6 10.8a15 15 0 0 0 6.6 6.6l2.2-2.2c.3-.3.7-.4 1-.2 1.1.4 2.3.6 3.6.6.6 0 1 .4 1 1V20c0 .6-.4 1-1 1A17 17 0 0 1 3 4c0-.6.4-1 1-1h3.5c.6 0 1 .4 1 1 0 1.3.2 2.5.6 3.6.1.3 0 .7-.2 1z"/></svg>
      <h3>TELEFON</h3>
      <p>7654321</p>
    </div>
    <div class="info-card" style="left:56px;top:392px;width:227px;height:216px;padding-top:26px">
      <svg width="58" height="58" viewBox="0 0 24 24"><path fill="none" stroke="var(--red)" stroke-width="1.3" stroke-linejoin="round" d="M22 2 2 10l8 3 3 8zM22 2 10 13"/></svg>
      <h3>MESSENGER</h3>
      <p>1-555-014-7700</p>
    </div>
    <div class="info-card" style="left:304px;top:392px;width:229px;height:216px;padding-top:32px">
      <svg width="62" height="44" viewBox="0 0 32 22"><rect width="32" height="22" fill="var(--red)"/><path fill="none" stroke="#fff" stroke-width="1.4" d="M0 0l16 12L32 0M0 22l12-11M32 22 20 11"/></svg>
      <h3>EMAIL</h3>
      <p><a href="#">mira@mirastudio.info</a></p>
    </div>
  </section>

  <footer class="site-footer">
    <div class="footer-brand">VMT</div>
    <div class="footer-social"><span></span><span class="square"></span></div>
    <div class="footer-rule"></div>
    <div class="footer-col" style="left:76px">VMT AG<br>Lindenweg 17<br>40210 Ortsbach</div>
    <div class="footer-col" style="left:458px">Tel.: +49 21 55 / 4 81 27 -00<br>info@vmt-pflegeloesung.de<br>&nbsp;vmt-pflegeloesung.de</div>
    <div class="footer-col" style="left:840px">Privacy<br>Datenschutz<br>Impressum</div>
  </footer>
</body>
</html>
```